Modern Spot UV Business Card design

We are a relatively new real estate agency. We need a business card that reflects the professionalism and prestige of our company but is also modern and fresh, based around our logo.
We would love to utilise spot UV.
Happy to let the designers use their imagination and see what they come up with (we're not very creative, so have no ideas for you, sorry) :-)
We'd like one for each staff member, but I've just provided one staff members photo here to avoid confusion.

Target Market(s)

Families

Industry/Entity Type

Real Estate Agent

Contact Information for Business Card

Colin Varga - Director & Principal
Mobile: 0491 527 806
Email: colin.varga@vbrokers.example.com.au
Phone: (08) 7364 9150
Fax: (08) 7364 9182
www.vargabrokersrealestate.example.com.au

Font styles to use
Other font styles liked:
• Kabel Dm BT

Requirements
Must have
• Contact details, logo, photo, spot UV
Nice to have
• Modern interesting features that will make people comment. Nothing too feminine nor too masculine.
Should not have
• No houses! Nothing typical of a real estate agent.

```html
<!DOCTYPE html>
<html lang="en">
<head>
<meta charset="utf-8">
<title>Varga Brokers Real Estate – Business Card</title>
<link rel="stylesheet" href="https://fonts.googleapis.com/css2?family=Arimo:wght@400;700&display=swap">
<style>
  :root {
    --backdrop: #c9c9c9;
    --paper: #ffffff;
    --ink: #111111;
    --ink-soft: #555555;
    --navy: #0b4c9c;
    --blue-mid: #3f78c0;
    --blue-light: #b9d0ea;
    --band-blue: #5b8fc7;
    --brand-blue: #1d5fae;
  }
  * { box-sizing: border-box; margin: 0; padding: 0; }
  html, body {
    width: 993px; height: 1200px; overflow: hidden;
    background: var(--backdrop);
    font-family: "Arimo", Arial, sans-serif;
  }
  .sheet {
    position: relative; width: 993px; height: 1200px;
    display: flex; flex-direction: column; align-items: center;
    justify-content: center; gap: 90px;
  }
  .card {
    position: relative; width: 860px; height: 478px;
    background: var(--paper); overflow: hidden;
    box-shadow: 0 6px 18px rgba(0,0,0,0.28);
  }
  .card-shapes { position: absolute; inset: 0; width: 100%; height: 100%; }

  .brand { position: absolute; }
  .brand-row { display: flex; align-items: center; gap: 10px; }
  .brand-dot {
    width: 22px; height: 22px; border-radius: 50%;
    background: var(--brand-blue); flex: none;
  }
  .brand-name {
    font-weight: 700; font-size: 34px; color: var(--brand-blue);
    letter-spacing: -0.5px; white-space: nowrap;
  }
  .brand-tagline {
    margin-top: 6px; margin-left: 32px;
    font-size: 15px; line-height: 1.05; color: var(--ink-soft);
  }

  .card-front .brand { left: 80px; top: 80px; }

  .name-banner {
    position: absolute; right: 0; top: 160px; width: 420px; height: 96px;
    color: #fff; text-align: right; padding: 20px 34px 0 0;
  }
  .name-banner svg { position: absolute; inset: 0; width: 100%; height: 100%; z-index: 0; }
  .person-name, .person-role { position: relative; z-index: 1; }
  .person-name { font-size: 32px; font-weight: 400; }
  .person-role { font-size: 17px; margin-top: 4px; }

  .contact {
    position: absolute; right: 34px; top: 292px;
    text-align: right; color: var(--ink); line-height: 1.3;
  }
  .contact-line { font-size: 18px; font-weight: 700; }
  .contact-label { margin-right: 6px; }
  .contact-web { font-size: 16px; font-weight: 700; }
  .contact-gap { height: 10px; }

  .card-back .band { position: absolute; left: 0; right: 0; background: var(--band-blue); }
  .band-top { top: 0; height: 130px; }
  .band-bottom { bottom: 0; height: 130px; }
  .card-back .brand {
    left: 50%; top: 50%; transform: translate(-50%, -50%);
  }
</style>
</head>
<body>
<main class="sheet">

  <section class="card card-front" aria-label="Business card front">
    <svg class="card-shapes" viewBox="0 0 860 478" preserveAspectRatio="none" aria-hidden="true">
      <defs>
        <linearGradient id="front-sweep" x1="0" y1="0.3" x2="1" y2="0.9">
          <stop offset="0" stop-color="#0b4c9c"/>
          <stop offset="0.45" stop-color="#3f78c0"/>
          <stop offset="1" stop-color="#b9d0ea"/>
        </linearGradient>
      </defs>
      <polygon points="0,300 860,110 860,478 0,478" fill="url(#front-sweep)"/>
    </svg>

    <div class="brand">
      <div class="brand-row">
        <span class="brand-dot"></span>
        <span class="brand-name">Varga Brokers Real Estate</span>
      </div>
      <p class="brand-tagline">Here with you for<br>every fresh start</p>
    </div>

    <div class="name-banner">
      <svg viewBox="0 0 420 96" preserveAspectRatio="none" aria-hidden="true">
        <polygon points="0,20 420,0 420,96 36,96 36,40" fill="#0b4c9c"/>
      </svg>
      <p class="person-name">Colin Varga</p>
      <p class="person-role">Director &amp; Principal</p>
    </div>

    <div class="contact">
      <p class="contact-line"><span class="contact-label">Phone :</span>(08) 7364 9150</p>
      <p class="contact-line"><span class="contact-label">Fax :</span>(08) 7364 9182</p>
      <p class="contact-line"><span class="contact-label">Mobile :</span>0491 527 806</p>
      <div class="contact-gap"></div>
      <p class="contact-web">colin.varga@vbrokers.example.com.au</p>
      <p class="contact-web">www.vargabrokersrealestate.example.com.au</p>
    </div>
  </section>

  <section class="card card-back" aria-label="Business card back">
    <div class="band band-top"></div>
    <div class="band band-bottom"></div>
    <div class="brand">
      <div class="brand-row">
        <span class="brand-dot"></span>
        <span class="brand-name">Varga Brokers Real Estate</span>
      </div>
      <p class="brand-tagline">Here with you for<br>every fresh start</p>
    </div>
  </section>

</main>
</body>
</html>
```